Landcape Construction Company needs a flyer to catch attention

A flyer that can be displayed at several different stores detailing our skills, work produced, experience and contact details. Information can be extracted from our website www.brvkw.co.nz. The flyer should feel very green, with addition of pics of work completed as well as stock images of lush green plants, lawns, landscape or similar. Needs to be eye catching with just enough information to express our experience and commitment to high standards

Target Market(s)

Residential
Landscape Architects

Industry/Entity Type

Landscaping

Font styles to use
Serif

Colors
abd037

Requirements
Must have
• Our logo
Experience
Services offered including pictures
All information avail on our website www.brvkw.co.nz
Nice to have
• stock images of lush greenery like a garden after fresh rainfall
Should not have
• Nothing comes to mind

```html
<!DOCTYPE html>
<html lang="en">
<head>
<meta charset="utf-8">
<title>Bracken Vale Landscape Works – Flyer</title>
<link rel="stylesheet" href="https://fonts.googleapis.com/css2?family=Roboto:wght@400;500;700&family=Roboto+Condensed:wght@500;700&family=Montserrat:wght@500;600&display=swap">
<style>
  :root {
    --leaf: #9bc850;
    --forest: #2e7a4a;
    --sand: #c3b497;
    --mist: #efeff2;
    --ink: #222222;
    --rule: #b9b9b9;
    --paper: #ffffff;
  }
  * { box-sizing: border-box; margin: 0; padding: 0; }
  html, body {
    width: 817px; height: 1200px; overflow: hidden;
    background: var(--paper);
  }
  .sheet {
    position: relative; width: 880px; height: 1300px;
    transform: scale(0.92841, 0.92308); transform-origin: 0 0;
    font-family: "Roboto", Arial, sans-serif; color: var(--ink);
  }
  .artwork { position: absolute; inset: 0; }
  .text { position: absolute; white-space: nowrap; }

  .intro { left: 50px; top: 86px; font-size: 10px; line-height: 11.6px; }

  .brand-name {
    position: absolute; text-align: center; color: var(--forest);
    font-family: "Roboto", Arial, sans-serif; font-weight: 500; font-size: 10.5px; line-height: 12px;
  }
  .brand-inside { left: 355px; top: 362px; width: 160px; }
  .brand-cover { left: 640px; top: 563px; width: 160px; }

  .contact { left: 320px; top: 418px; width: 236px; text-align: center; color: var(--forest); font-weight: 500; }
  .contact .phone { font-size: 31px; line-height: 36px; font-weight: 700; letter-spacing: 0.3px; }
  .contact .email { font-size: 23.5px; line-height: 28px; }

  .tagline {
    right: 70px; top: 366px; text-align: right; color: var(--sand);
    font-family: "Montserrat", Arial, sans-serif; font-weight: 600;
    font-size: 29px; line-height: 33px; letter-spacing: 2px;
  }

  .quality-title {
    left: 58px; top: 746px; color: var(--forest);
    font-family: "Montserrat", Arial, sans-serif; font-weight: 600;
    font-size: 17px; line-height: 20px; letter-spacing: 1.4px;
  }
  .about { color: var(--forest); font-size: 10.4px; line-height: 11.6px; }
  .about-values { left: 47px; top: 835px; }
  .about-accreditation { left: 47px; top: 966px; }
  .about-process { right: 602px; top: 1040px; text-align: right; }

  .services-title {
    left: 338px; top: 716px; color: var(--sand);
    font-family: "Montserrat", Arial, sans-serif; font-weight: 600;
    font-size: 18px; letter-spacing: 1px;
  }
  .services-intro { left: 329px; top: 739px; font-size: 10px; line-height: 11.6px; }
  .service-list { left: 330px; top: 834px; width: 175px; list-style: none; }
  .service-list li {
    font-family: "Roboto Condensed", Arial, sans-serif; font-weight: 700;
    font-size: 15px; line-height: 26px; height: 27px; padding-left: 5px;
    border-bottom: 1.5px solid var(--rule); color: var(--ink);
  }
</style>
</head>
<body>
<main class="sheet">
  <svg class="artwork" width="880" height="1300" viewBox="0 0 880 1300">
    <defs>
      <clipPath id="outside-spread"><rect x="20" y="22" width="842" height="595"/></clipPath>
      <clipPath id="inside-spread"><rect x="20" y="680" width="842" height="596"/></clipPath>
      <linearGradient id="tone-bench" x1="0" y1="0" x2="1" y2="1"><stop offset="0" stop-color="#d9dbdc"/><stop offset="0.6" stop-color="#a7a9a8"/><stop offset="1" stop-color="#8a6a48"/></linearGradient>
      <linearGradient id="tone-pool" x1="0" y1="0" x2="1" y2="1"><stop offset="0" stop-color="#6b8a5a"/><stop offset="0.35" stop-color="#c9c7c2"/><stop offset="0.7" stop-color="#7fb8bd"/><stop offset="1" stop-color="#8c8781"/></linearGradient>
      <radialGradient id="tone-leaf" cx="0.5" cy="0.45" r="0.6"><stop offset="0" stop-color="#7fc24a"/><stop offset="0.7" stop-color="#4d9a32"/><stop offset="1" stop-color="#2f6e25"/></radialGradient>
      <linearGradient id="tone-planter" x1="0" y1="0" x2="1" y2="1"><stop offset="0" stop-color="#5f8a3c"/><stop offset="0.5" stop-color="#a8503a"/><stop offset="1" stop-color="#9a9a96"/></linearGradient>
      <linearGradient id="tone-drive" x1="0" y1="0" x2="0" y2="1"><stop offset="0" stop-color="#5a5048"/><stop offset="0.3" stop-color="#8f8e8b"/><stop offset="1" stop-color="#76757a"/></linearGradient>
      <linearGradient id="tone-lawn" x1="0" y1="0" x2="1" y2="1"><stop offset="0" stop-color="#cfc7bb"/><stop offset="0.4" stop-color="#6f9e3c"/><stop offset="0.75" stop-color="#a8ad9e"/><stop offset="1" stop-color="#d6d0c6"/></linearGradient>
      <linearGradient id="tone-timber" x1="0" y1="0" x2="0" y2="1"><stop offset="0" stop-color="#dfeec9"/><stop offset="0.45" stop-color="#c2d99a"/><stop offset="0.55" stop-color="#c88a45"/><stop offset="1" stop-color="#a86a2c"/></linearGradient>
      <linearGradient id="tone-pavers" x1="0" y1="0" x2="1" y2="1"><stop offset="0" stop-color="#8f8f8f"/><stop offset="1" stop-color="#6d6d6d"/></linearGradient>
    </defs>

    <g clip-path="url(#outside-spread)">
      <rect class="panel" x="20" y="22" width="274" height="595" fill="var(--paper)"/>
      <rect class="panel" x="294" y="22" width="284" height="595" fill="var(--leaf)"/>
      <rect class="panel" x="578" y="22" width="284" height="595" fill="var(--paper)"/>
      <line x1="294" y1="22" x2="294" y2="617" stroke="var(--ink)" stroke-width="1"/>
      <line x1="578" y1="22" x2="578" y2="617" stroke="var(--ink)" stroke-width="1"/>

      <circle cx="182" cy="26" r="13" fill="var(--leaf)"/>
      <circle cx="260" cy="160" r="49" fill="url(#tone-bench)" role="img" aria-label="Photo of a paved courtyard with a timber bench"/>
      <circle cx="232" cy="228" r="22" fill="var(--forest)"/>
      <circle cx="246" cy="316" r="32" fill="var(--mist)"/>
      <circle cx="28" cy="360" r="34" fill="var(--leaf)"/>
      <circle cx="145" cy="462" r="125" fill="url(#tone-pool)" role="img" aria-label="Photo of a pool surrounded by grey timber decking and steps"/>
      <circle cx="230" cy="572" r="32" fill="var(--forest)"/>

      <circle class="brand-mark" cx="435" cy="322" r="31" fill="var(--forest)"/>
      <line x1="340" y1="411" x2="535" y2="411" stroke="var(--forest)" stroke-width="3"/>
      <line x1="340" y1="490" x2="535" y2="490" stroke="var(--forest)" stroke-width="3"/>

      <circle cx="840" cy="55" r="45" fill="var(--leaf)"/>
      <circle cx="600" cy="105" r="42" fill="var(--forest)"/>
      <circle cx="702" cy="238" r="158" fill="url(#tone-leaf)" role="img" aria-label="Photo of fresh green leaves covered in raindrops"/>
      <circle cx="615" cy="403" r="22" fill="var(--leaf)"/>
      <circle cx="583" cy="542" r="33" fill="var(--mist)"/>
      <rect x="826" y="370" width="4" height="88" fill="var(--leaf)"/>
      <circle class="brand-mark" cx="720" cy="525" r="35" fill="var(--forest)"/>
    </g>
    <rect x="20" y="22" width="842" height="595" fill="none" stroke="var(--ink)" stroke-width="1"/>

    <g clip-path="url(#inside-spread)">
      <rect class="panel" x="20" y="680" width="284" height="596" fill="var(--leaf)"/>
      <rect class="panel" x="304" y="680" width="283" height="596" fill="var(--paper)"/>
      <rect class="panel" x="587" y="680" width="275" height="596" fill="var(--leaf)"/>
      <line x1="304" y1="680" x2="304" y2="1276" stroke="var(--ink)" stroke-width="1"/>
      <line x1="587" y1="680" x2="587" y2="1276" stroke="var(--ink)" stroke-width="1"/>

      <circle cx="125" cy="688" r="18" fill="var(--forest)"/>
      <rect x="49" y="746" width="3" height="76" fill="var(--paper)"/>
      <circle cx="274" cy="782" r="11" fill="var(--paper)"/>
      <circle cx="270" cy="868" r="56" fill="url(#tone-planter)" role="img" aria-label="Photo of brick planter boxes beside stepping stones"/>
      <circle cx="92" cy="1127" r="78" fill="url(#tone-drive)" role="img" aria-label="Photo of an exposed aggregate driveway"/>
      <circle cx="140" cy="1245" r="42" fill="var(--forest)"/>
      <circle cx="229" cy="1218" r="7" fill="var(--paper)"/>

      <rect x="330" y="718" width="3" height="16" fill="var(--leaf)"/>

      <circle cx="848" cy="770" r="62" fill="var(--forest)"/>
      <circle cx="646" cy="825" r="115" fill="url(#tone-lawn)" role="img" aria-label="Photo of a lawn with a sprinkler and concrete edging beside pebbles"/>
      <circle cx="772" cy="850" r="14" fill="var(--paper)"/>
      <circle cx="785" cy="1030" r="85" fill="url(#tone-timber)" role="img" aria-label="Photo of a timber tabletop against soft green foliage"/>
      <circle cx="661" cy="1015" r="7" fill="var(--paper)"/>
      <circle cx="542" cy="1072" r="14" fill="var(--leaf)"/>
      <circle cx="590" cy="1152" r="81" fill="url(#tone-pavers)" role="img" aria-label="Photo of large grey concrete pavers"/>
      <circle cx="705" cy="1235" r="33" fill="var(--forest)"/>
      <circle cx="848" cy="1160" r="24" fill="var(--paper)"/>
    </g>
    <rect x="20" y="680" width="842" height="596" fill="none" stroke="var(--ink)" stroke-width="1"/>
  </svg>

  <p class="text intro">With more than 25 years<br>experience in the landscaping<br>industry, Bracken Vale Landscape<br>Works offers services to large or<br>small residential and commercial<br>projects. Based in Canterbury,<br>we are locally owned and<br>operated. Whether you have a<br>blank canvas or are looking to<br>rejuvenate your property we are<br>able to advise and make the<br>process easy and stress free.<br>From paving, pergolas and<br>decks to concrete or planting<br>your dream garden we have<br>the expertise to help.</p>

  <p class="brand-name brand-inside">Bracken Vale<br>Landscape Works Ltd</p>

  <div class="text contact">
    <p class="phone">021 555 0142</p>
    <p class="email">hello@brvkw.co.nz</p>
  </div>

  <h1 class="text tagline">MODESTY<br>OF<br>PERFECTION</h1>
  <p class="brand-name brand-cover">Bracken Vale<br>Landscape Works Ltd</p>

  <h2 class="text quality-title">QUALITY<br>WORKMANSHIP<br>AT AFFORDABLE<br>RATE</h2>
  <p class="text about about-values">Our company is built on honesty,<br>teamwork, sound knowledge and<br>a determination to provide our<br>customers with the highest<br>quality product and service. We<br>are a small team of highly skilled,<br>dedicated and reliable professionals<br>who complete projects efficiently and<br>with outstanding workmanship.</p>
  <p class="text about about-accreditation">We hold Pavecrest Pro Accreditation status making<br>us preferred installers of this paving system.<br>To achieve this we had to show we had a solid<br>understanding of the system and the skill set to<br>ensure workmanship was held to the highest<br>standard.</p>
  <p class="text about about-process">How we work is simple. We will<br>listen, get a clear idea of your<br>vision and offer practical<br>advice in order to achieve<br>the best outcome within<br>your budget and scope.<br>An initial consultation<br>is free so give us a<br>call and let's chat<br>about getting the<br>best solution to your<br>landscaping needs.</p>

  <h2 class="text services-title">SERVICES</h2>
  <p class="text services-intro">As a full construction landscaping company,<br>we formally offer the following services.<br>However, we regularly work with clients<br>who want something a little out of the box.<br>If there is something in particular you are<br>after, we are happy to discuss options<br>with you</p>
  <ul class="text service-list">
    <li>PATIOS</li>
    <li>PAVING</li>
    <li>CONCRETE</li>
    <li>WATER FEATURES</li>
    <li>DECKING</li>
    <li>FENCING</li>
    <li>BOARDWALKS</li>
    <li>TIMBER</li>
    <li>PLANTER BOXES</li>
    <li>PERGOLAS</li>
    <li>RETAINING WALLS</li>
    <li>GARDENS &amp; LAWNS</li>
    <li>IRRIGATION</li>
    <li>PROJECT MANAGEMENT</li>
    <li>CONSULTATION</li>
  </ul>
</main>
</body>
</html>
```